Criação de Layout de Post para Imóveis
A empresa queria:
" Lume Fin uma empresa especializada em soluções no segmento de crédito imobiliário. Como correspondente bancário atuamos com as principais instituições financeiras do pais, oferecemos as melhores condições para seu credito imobiliário. Nosso principal foco é buscar as melhores taxas, custos, conveniências, prazos e demais circunstâncias que melhor possa lhe atender. "

```html
<!DOCTYPE html>
<html lang="pt-BR">
<head>
<meta charset="UTF-8">
<title>Lume Fin – Soluções em crédito imobiliário</title>
<link rel="stylesheet" href="https://fonts.googleapis.com/css2?family=Montserrat:wght@300;400;500&display=swap">
<style>
  :root {
    --charcoal: #323232;
    --gold: #c8964f;
    --gold-light: #e2b574;
    --gold-dark: #a9773a;
    --white: #ffffff;
    --text-soft: #e6e6e6;
  }
  html, body {
    margin: 0;
    padding: 0;
    width: 1200px;
    height: 1200px;
    overflow: hidden;
    background: var(--charcoal);
  }
  .post {
    position: relative;
    width: 1200px;
    height: 1200px;
    background: var(--charcoal);
    font-family: "Montserrat", Arial, sans-serif;
    color: var(--white);
    overflow: hidden;
  }
  .decor-area {
    position: absolute;
    inset: 0;
    background:
      radial-gradient(ellipse 520px 420px at 0% 8%, rgba(200,150,79,0.55) 0%, rgba(200,150,79,0) 100%),
      radial-gradient(ellipse 480px 520px at 100% 100%, rgba(200,150,79,0.45) 0%, rgba(200,150,79,0) 100%),
      var(--charcoal);
  }
  .family-photo {
    position: absolute;
    left: 232px;
    top: 236px;
    width: 712px;
    height: 712px;
    border-radius: 50%;
    background: radial-gradient(circle at 60% 35%, #f3e6cf 0%, #e2c9a3 35%, #b98f68 65%, #6b5244 100%);
  }
  .brand {
    position: absolute;
    left: 650px;
    top: 62px;
    display: flex;
    flex-direction: column;
  }
  .brand__name {
    display: flex;
    align-items: center;
    gap: 16px;
    font-size: 60px;
    font-weight: 500;
    line-height: 1;
    color: var(--white);
  }
  .brand__dot {
    width: 26px;
    height: 26px;
    border-radius: 50%;
    background: var(--gold);
  }
  .brand__tagline {
    margin-top: 16px;
    font-size: 20px;
    font-weight: 400;
    letter-spacing: 1px;
    color: var(--gold-light);
    text-transform: uppercase;
  }
  .headline {
    position: absolute;
    left: 72px;
    top: 950px;
    margin: 0;
    font-size: 50px;
    font-weight: 300;
    line-height: 1.2;
    color: var(--white);
  }
  .lead {
    position: absolute;
    left: 72px;
    top: 1090px;
    width: 620px;
    margin: 0;
    font-size: 17px;
    font-weight: 400;
    line-height: 1.65;
    color: var(--text-soft);
  }
</style>
</head>
<body>
  <main class="post">
    <div class="decor-area" role="img" aria-label="Faixas curvas decorativas em dourado e branco atravessando o fundo escuro"></div>

    <div class="family-photo" role="img" aria-label="Fotografia de uma família sorridente: pai, mãe e duas filhas abraçados ao ar livre"></div>

    <div class="brand">
      <span class="brand__name"><span class="brand__dot"></span>Lume Fin</span>
      <span class="brand__tagline">Soluções em crédito imobiliário</span>
    </div>

    <h1 class="headline">Soluções no segmento<br>de crédito imobiliário</h1>
    <p class="lead">Nosso principal foco é buscar as melhores taxas, custos, conveniências, prazos e demais circunstâncias que melhor possa lhe atender.</p>
  </main>
</body>
</html>
```